Falverino’s Artisan Pizzeria Menu Contest

I’m looking for a menu design for a new pizzeria - it’s farm to table type of restaurant - more upscale than a typical pizzeria - white washed wood interior with some industrial accents - I am looking for a creative menu layout using the attached sample menu items -
Falverino’s is an artisanal pizzeria with an atmosphere that will make you feel at home for any situation, first date, anniversary, business lunch, boys night out or girls night out with a menu inspired by the idea of a simple honest cooking paired with fresh – quality ingredients. Full service dining experience that is still casual but dedicated to extraordinary hospitality.
While developing the menu we have created a network of amazing farms and purveyors to supply our restaurant with fresh milled 100% California flour for our hand crafted dough, as well as sustainably farmed organic produce, meats and cheeses.
The menu includes classics like the Margherita pizza to daily seasonal specials, fresh salads to rustic small plates including moms meatball recipe to a fresh local burrata with handmade bread. Each dish reflects our passion for sourcing the freshest quality local ingredients.
To compliment the menu, Falverino’s serves an extensive wine list with selections focusing on Italian varietals. The cocktail program has been carefully crafted to offer something to entice ever palate and the beer list has unique selections of the world’s finest brewers.
Target Market(s)
25-45 year old men and women
Industry/Entity Type
American Restaurant
Requirements
Must have
- professional tone
Nice to have
- a balance of elegance and industrial (rustic)
Should not have
- photos or playful graphics etc..

```html
<!DOCTYPE html>
<html lang="en">
<head>
<meta charset="utf-8">
<title>Falverino’s Artisan Pizzeria — Menu</title>
<link rel="stylesheet" href="https://fonts.googleapis.com/css2?family=Anton&family=Questrial&family=Lato:ital@1&display=swap">
<style>
  :root {
    --ink: #ffffff;
    --muted: #d9d9d9;
    --faint: #9a9a9a;
    --ribbon: #e4474f;
    --night: #0b0b0b;
    --ember: #3a1208;
    --flame: #c4471a;
    --glow: #f2a32c;
    --row: 34.3px;
  }
  * { box-sizing: border-box; margin: 0; padding: 0; }
  html, body { width: 1200px; height: 847px; overflow: hidden; background: var(--night); }
  .menu {
    position: relative; width: 1200px; height: 847px; overflow: hidden;
    color: var(--ink); font-family: "Questrial", sans-serif;
  }
  .menu-backdrop {
    position: absolute; inset: 0;
    background:
      radial-gradient(ellipse 230px 260px at 610px 90px, rgba(242,163,44,.85), rgba(196,71,26,.55) 45%, transparent 75%),
      radial-gradient(ellipse 330px 420px at 600px 300px, rgba(130,40,14,.75), transparent 70%),
      radial-gradient(ellipse 480px 300px at 560px 560px, rgba(60,20,10,.6), transparent 75%),
      linear-gradient(180deg, #120604 0%, var(--night) 60%, #050505 100%);
  }
  .menu-frame, .column-rules { position: absolute; inset: 0; }

  .section { position: absolute; }
  .section-head { position: relative; height: 40px; }
  .section-title {
    position: absolute; top: 0; font-family: "Anton", sans-serif; font-size: 35px;
    line-height: 40px; letter-spacing: .5px; color: var(--ink); white-space: nowrap;
  }
  .ribbon { position: absolute; top: 0; }

  .menu-list { list-style: none; position: absolute; }
  .menu-item { position: relative; height: var(--row); }
  .item-name { display: block; font-size: 20px; line-height: 22px; letter-spacing: .3px; white-space: nowrap; }
  .item-price { position: absolute; right: 0; top: 0; font-size: 20px; line-height: 22px; letter-spacing: .5px; }
  .item-desc {
    font-family: "Lato", sans-serif; font-style: italic; font-size: 8px; line-height: 10px;
    color: var(--muted); white-space: nowrap;
  }
  .item-desc.wrap { white-space: normal; }
  .item-price.dim { color: #2a2a2a; }

  .brand {
    position: absolute; left: 457px; top: 96px; width: 267px; text-align: center;
  }
  .brand-name { font-family: "Anton", sans-serif; font-size: 52px; line-height: 60px; color: var(--ink); letter-spacing: 2px; }
  .brand-tag { font-family: "Questrial", sans-serif; font-size: 12px; letter-spacing: 3px; text-transform: uppercase; color: var(--ink); margin-top: 6px; }
</style>
</head>
<body>
<main class="menu">
  <div class="menu-backdrop" role="img" aria-label="Photograph of wood-fired oven flames rising over a pizza"></div>

  <svg class="menu-frame" width="1200" height="847" viewBox="0 0 1200 847" aria-hidden="true">
    <path d="M584 822 H50 A25 25 0 0 0 25 797 V49 A25 25 0 0 0 50 24 H1150 A25 25 0 0 0 1175 49 V797 A25 25 0 0 0 1150 822 H622"
          fill="none" stroke="#ffffff" stroke-width="2"/>
  </svg>
  <svg class="column-rules" width="1200" height="847" viewBox="0 0 1200 847" aria-hidden="true">
    <line x1="401" y1="38" x2="401" y2="813" stroke="#ffffff" stroke-width="2.5" stroke-dasharray="16 10"/>
    <line x1="799" y1="38" x2="799" y2="813" stroke="#ffffff" stroke-width="2.5" stroke-dasharray="16 10"/>
  </svg>

  <!-- Appetizers -->
  <section class="section appetizers" style="left:0;top:107px;width:400px">
    <div class="section-head">
      <svg class="ribbon" style="left:45px" width="80" height="40"><polygon points="0,0 80,0 80,40 0,40 14,20" fill="var(--ribbon)"/></svg>
      <h2 class="section-title" style="left:138px">APPETIZERS</h2>
      <svg class="ribbon" style="left:305px" width="79" height="40"><polygon points="0,0 79,0 65,20 79,40 0,40" fill="var(--ribbon)"/></svg>
    </div>
    <ul class="menu-list" style="left:45px;top:58px;width:328px">
      <li class="menu-item" style="height:46px"><span class="item-name">Brussels</span><p class="item-desc wrap">Pan Seared brussel sprouts with a drizzle of blasamic reduction and parm and bread crumbs</p></li>
      <li class="menu-item"><span class="item-name">Meatballs</span><span class="item-price">$13.00</span><p class="item-desc">moms meatballs handmade secret recipe for over 75 years</p></li>
      <li class="menu-item"><span class="item-name">Mussels</span><span class="item-price">$15.00</span><p class="item-desc">New Zealand Mussels in a tomato broth</p></li>
      <li class="menu-item"><span class="item-name">Romanesco</span><span class="item-price">$11.00</span><p class="item-desc">Flash fried romanesco served atop a spicy aioli</p></li>
      <li class="menu-item"><span class="item-name">Chicken Wings</span><span class="item-price">$10.00</span><p class="item-desc">Italian fried chicken wings with a kick</p></li>
      <li class="menu-item"><span class="item-name">Burrata</span><span class="item-price">$13.00</span><p class="item-desc">Local burrata served with apples grapes and fresh made bread</p></li>
    </ul>
  </section>

  <!-- Salads -->
  <section class="section salads" style="left:0;top:418px;width:400px">
    <div class="section-head">
      <svg class="ribbon" style="left:45px" width="12" height="36"><rect width="12" height="36" fill="var(--ribbon)"/></svg>
      <h2 class="section-title" style="left:85px;top:-2px">SALADS</h2>
      <svg class="ribbon" style="left:208px" width="172" height="36"><rect width="172" height="36" fill="var(--ribbon)"/></svg>
    </div>
    <ul class="menu-list" style="left:45px;top:45px;width:328px">
      <li class="menu-item" style="height:46px"><span class="item-name">Chopped</span><span class="item-price">$13.00</span><p class="item-desc wrap" style="font-size:9px">Lettuce mix with tomato, onion, peppers, pepperoni, chick peas, fresh mozz, italian herb ving</p></li>
      <li class="menu-item"><span class="item-name">Caesar Salad</span><span class="item-price">$11.00</span><p class="item-desc" style="color:var(--faint)">Traditional caesar salad rich and creamy extra shaved parmesan</p></li>
      <li class="menu-item"><span class="item-name">Farm Salad</span><span class="item-price">$15.00</span><p class="item-desc" style="color:var(--faint)">Seasonal farmers market salad</p></li>
      <li class="menu-item"><span class="item-name">Grilled Little Gem</span><span class="item-price">$11.00</span><p class="item-desc" style="color:var(--faint)">Grilled little gems with bacon, tomato, red onions and blue cheese dressing</p></li>
      <li class="menu-item"><span class="item-name">Spinach and Arugula</span><span class="item-price">$12.00</span><p class="item-desc" style="color:var(--faint)">Spinach and argula red pepperstossed in a lemon ving and housemade croutons</p></li>
    </ul>
  </section>

  <!-- Dairy Soup -->
  <section class="section soup" style="left:0;top:675px;width:400px">
    <div class="section-head">
      <svg class="ribbon" style="left:40px" width="77" height="42"><polygon points="0,0 77,0 77,42 0,42 14,21" fill="var(--ribbon)"/></svg>
      <h2 class="section-title" style="left:127px">DAIRY SOUP</h2>
      <svg class="ribbon" style="left:298px" width="78" height="42"><polygon points="0,0 78,0 64,21 78,42 0,42" fill="var(--ribbon)"/></svg>
    </div>
    <ul class="menu-list" style="left:52px;top:52px;width:315px">
      <li class="menu-item"><span class="item-name">Example Tomato Bis</span><span class="item-price dim">$8.00</span></li>
    </ul>
  </section>

  <!-- Brand -->
  <header class="brand">
    <h1 class="brand-name">Falverino’s</h1>
    <p class="brand-tag">Artisan Pizzeria</p>
  </header>

  <!-- Pizzas -->
  <section class="section pizzas" style="left:0;top:290px;width:800px">
    <div class="section-head" style="height:60px">
      <svg class="ribbon" style="left:428px" width="90" height="60"><polygon points="0,0 90,0 90,60 0,60 16,30" fill="var(--ribbon)"/></svg>
      <h2 class="section-title" style="left:528px;font-size:54px;line-height:60px">PIZZAS</h2>
      <svg class="ribbon" style="left:680px" width="91" height="60"><polygon points="0,0 91,0 75,30 91,60 0,60" fill="var(--ribbon)"/></svg>
    </div>
    <ul class="menu-list" style="left:428px;top:79px;width:328px">
      <li class="menu-item" style="height:38.5px"><span class="item-name">Margherita</span><span class="item-price">$14.00</span><p class="item-desc">Classic Margherita pizza - Fresh Mozz Tomato Sauce and Basil</p></li>
      <li class="menu-item" style="height:38.5px"><span class="item-name">Organic Sausage</span><span class="item-price">$16.00</span><p class="item-desc">Organic Sausage Housemade Red Sauce Mozz hint of fennel</p></li>
      <li class="menu-item" style="height:38.5px"><span class="item-name">Pepperoni</span><span class="item-price">$16.00</span><p class="item-desc">Hollis Pepperoni - Housemade Red Sauce Mozz hint of fennel</p></li>
      <li class="menu-item" style="height:38.5px"><span class="item-name">Salumi And Burrata</span><span class="item-price">$17.00</span><p class="item-desc">Salumi dried Red Sauce finished with whipped burrata</p></li>
      <li class="menu-item" style="height:38.5px"><span class="item-name">Daily Special</span><span class="item-price">$17.00</span></li>
      <li class="menu-item" style="height:38.5px"><span class="item-name">Mushroom</span><span class="item-price">$15.00</span><p class="item-desc">Shaved mushrooms with a Paemesan cream and melted onions</p></li>
      <li class="menu-item" style="height:38.5px"><span class="item-name">Prosciutto Formaggi</span><span class="item-price">$16.00</span><p class="item-desc">Parma Prosciutto Parmesan cream with aged alpine and gruyere finished with an organic egg</p></li>
      <li class="menu-item" style="height:38.5px"><span class="item-name">Quarttro Formaggi</span><span class="item-price">$15.00</span><p class="item-desc">Four cheese combination - mozz - fontina - parm cream and gruyere chile flakes and oregano</p></li>
      <li class="menu-item" style="height:38.5px"><span class="item-name">Farmers Pizza</span><span class="item-price">$17.00</span><p class="item-desc">Seasonal vegetables cream sauce and variety of cheese</p></li>
      <li class="menu-item" style="height:38.5px"><span class="item-name">Keto Friendly</span><span class="item-price">$17.00</span><p class="item-desc">Cauliflower crust, spanach and kale, parm cream sauce</p></li>
    </ul>
  </section>

  <!-- Sandwiches -->
  <section class="section sandwiches" style="left:800px;top:111px;width:400px">
    <div class="section-head">
      <svg class="ribbon" style="left:24px" width="13" height="38"><rect width="13" height="38" fill="var(--ribbon)"/></svg>
      <h2 class="section-title" style="left:50px;top:-1px">SANDWICHES</h2>
      <svg class="ribbon" style="left:245px" width="114" height="38"><rect width="114" height="38" fill="var(--ribbon)"/></svg>
    </div>
    <ul class="menu-list" style="left:24px;top:50px;width:329px">
      <li class="menu-item"><span class="item-name">Italian Sub</span><span class="item-price">$13.00</span><p class="item-desc">Prociutto, salumi, turkey, provolone, lettuce and herb aioli with spicy gardenia</p></li>
      <li class="menu-item"><span class="item-name">Turkey Sandwich</span><span class="item-price">$12.00</span><p class="item-desc">Housemade bread - turkey, cheddar cheese, butter lettuce, tomato and mustard aioli</p></li>
      <li class="menu-item"><span class="item-name">Meatball Sub</span><span class="item-price">$13.00</span><p class="item-desc">Moms meatballs melted provolone on a housemade roll</p></li>
      <li class="menu-item"><span class="item-name">Plantwise Burger</span><span class="item-price">$14.00</span><p class="item-desc">Housemade bun - arugula, tomato, onion and a sundried tomato spread</p></li>
      <li class="menu-item"><span class="item-name">Chicken Sandwich</span><span class="item-price">$13.00</span><p class="item-desc">Fried chicken or chicken breast, provolone, argula, tomato, served with a spicy aioli</p></li>
    </ul>
  </section>

  <!-- Crusts -->
  <section class="section crusts" style="left:800px;top:385px;width:400px">
    <div class="section-head">
      <svg class="ribbon" style="left:15px" width="98" height="40"><polygon points="0,0 98,0 98,40 0,40 16,20" fill="var(--ribbon)"/></svg>
      <h2 class="section-title" style="left:133px">CRUSTS</h2>
      <svg class="ribbon" style="left:255px" width="97" height="40"><polygon points="0,0 97,0 81,20 97,40 0,40" fill="var(--ribbon)"/></svg>
    </div>
    <ul class="menu-list" style="left:18px;top:53px;width:316px">
      <li class="menu-item"><span class="item-name">Tradition</span><span class="item-price" style="left:260px;right:auto">$</span><p class="item-desc">Original crust you can't miss</p></li>
      <li class="menu-item"><span class="item-name">Gluten Free</span><span class="item-price">$3.00</span><p class="item-desc">best gluten friendly crust on the west coast</p></li>
      <li class="menu-item"><span class="item-name">Cauliflower</span><span class="item-price">$3.00</span><p class="item-desc">Vegans have needs</p></li>
    </ul>
  </section>

  <!-- Dips -->
  <section class="section dips" style="left:800px;top:595px;width:400px">
    <div class="section-head">
      <svg class="ribbon" style="left:18px" width="12" height="36"><rect width="12" height="36" fill="var(--ribbon)"/></svg>
      <h2 class="section-title" style="left:51px;top:-2px">DIPS</h2>
      <svg class="ribbon" style="left:133px" width="220" height="36"><rect width="220" height="36" fill="var(--ribbon)"/></svg>
    </div>
    <ul class="menu-list" style="left:18px;top:43px;width:316px">
      <li class="menu-item" style="height:20.3px"><span class="item-name">Ranch</span><span class="item-price">$1.00</span></li>
      <li class="menu-item" style="height:20.3px"><span class="item-name">Tomato Sauce</span><span class="item-price">$1.00</span></li>
      <li class="menu-item" style="height:20.3px"><span class="item-name">Spicy Dip</span><span class="item-price">$1.00</span></li>
    </ul>
  </section>
</main>
</body>
</html>
```